Flyer für einen ambulanten Pflegedienst
Zielgruppe
Wir sind ein ambulanter Pflegedienst und suchen ansprechende Designs und Vorlagen für unsere Flyer. Die Zielgruppe sind pflegebedürftige ältere Menschen und deren Angehörigen. Die Flyer sollen in Briefkästen, bei Ärzten, Krankenhäusern, Physiotherapiepraxen etc. verteilt werden.
Aufgabenstellung
Ich bin offen für Vorschläge und habe keine bestimmten Vorstellungen.

```html
<!DOCTYPE html>
<html lang="de">
<head>
<meta charset="utf-8">
<title>Pflegedienst Auenhaus – Flyer</title>
<link href="https://fonts.googleapis.com/css2?family=Bebas+Neue&family=Nunito:wght@400;600;700;800&display=swap" rel="stylesheet">
<style>
  :root{
    --green-dark:#0b7a50;
    --green-light:#8fcf85;
    --green-pale:#f3f8ef;
    --card-line:#b9e0b2;
    --text:#2a2a2a;
    --white:#ffffff;
    --backdrop:#e4e4e4;
  }
  *{margin:0;padding:0;box-sizing:border-box}
  html,body{width:1200px;height:1117px;overflow:hidden;background:var(--backdrop)}
  body{font-family:"Nunito",sans-serif;color:var(--text)}
  .flyer{position:absolute;left:215px;top:14px;width:770px;height:1089px;background:var(--white);overflow:hidden}
  .flyer-shapes{position:absolute;inset:0}
  .service-icons{position:absolute;inset:0;z-index:2;pointer-events:none}
  .abs{position:absolute}
  .brand{left:54px;top:36px;display:flex;align-items:center;gap:10px}
  .brand-dot{width:40px;height:40px;border-radius:50%;background:var(--green-dark)}
  .brand-name{font-weight:800;font-size:25px;line-height:27px;color:var(--green-dark)}
  .headline{left:407px;top:42px;width:350px;font-family:"Bebas Neue",sans-serif;font-size:39px;line-height:36px;color:var(--white);letter-spacing:.3px;font-weight:400}
  .tag{left:408px;top:228px;width:324px;height:32px;background:var(--green-light);border-radius:3px;color:var(--white);font-weight:800;font-size:19px;line-height:32px;text-align:center}
  .intro{left:408px;top:268px;width:296px;font-size:12.6px;line-height:16.3px}
  .section-title{left:0;width:770px;top:520px;text-align:center;font-weight:800;font-size:20px;color:var(--green-dark)}
  .section-lead{left:60px;width:650px;top:548px;text-align:center;font-size:12.6px;line-height:16.6px}
  .card{top:641px;width:224px;height:287px;border:1px solid var(--card-line);z-index:1;background:var(--white)}
  .card-title{position:absolute;left:0;right:0;top:55px;text-align:center;font-weight:800;font-size:14.6px;line-height:18px;color:var(--green-dark)}
  .card-rule{position:absolute;left:37px;right:37px;top:99px;height:1px;background:var(--green-light)}
  .card-text{position:absolute;left:15px;right:15px;top:112px;text-align:center;font-size:12.3px;line-height:14.8px}
  .claim{right:55px;top:951px;font-weight:800;font-size:21px;color:var(--green-dark)}
  .claim span{color:var(--green-light)}
  .contact-call{left:44px;top:1021px;color:var(--white);font-weight:800}
  .contact-call .label{font-size:17px;line-height:22px}
  .contact-call .phone{display:flex;align-items:center;gap:8px;font-size:22px;line-height:28px;margin-top:2px}
  .contact-list{top:1016px;color:var(--white);font-size:14px;line-height:23px}
  .contact-list li{list-style:none;display:flex;align-items:center;gap:7px;white-space:nowrap}
  .contact-list li.plain{padding-left:19px}
  .contact-list svg{flex:none}
</style>
</head>
<body>
<main class="flyer">
  <svg class="flyer-shapes" width="770" height="1089" viewBox="0 0 770 1089">
    <defs>
      <linearGradient id="photoTone" x1="0" y1="0" x2="1" y2="1">
        <stop offset="0" stop-color="#c8b596"/>
        <stop offset=".45" stop-color="#3d8cc6"/>
        <stop offset=".75" stop-color="#d9cfc2"/>
        <stop offset="1" stop-color="#eee9e1"/>
      </linearGradient>
      <clipPath id="photoClip"><rect x="0" y="119" width="400" height="420"/></clipPath>
    </defs>
    <rect x="0" y="205" width="770" height="295" fill="var(--green-pale)"/>
    <path d="M402 16 H770 V205 H330 V119 H350 Q372 119 377 95 L385 36 Q390 16 402 16 Z" fill="var(--green-dark)"/>
    <g clip-path="url(#photoClip)">
      <circle cx="140" cy="280" r="244" fill="var(--white)"/>
    </g>
    <circle cx="140" cy="280" r="240" fill="none" stroke="var(--green-light)" stroke-width="3" clip-path="url(#photoClip)"/>
    <g clip-path="url(#photoClip)">
      <circle cx="140" cy="280" r="232" fill="url(#photoTone)" role="img" aria-label="Foto: Pflegekraft hält lächelnd die Hand einer älteren Patientin"/>
    </g>
    <circle cx="726" cy="456" r="11" fill="var(--green-light)"/>
    <circle cx="765" cy="486" r="26" fill="var(--green-dark)"/>
    <circle cx="706" cy="506" r="11" fill="var(--green-dark)"/>
    <circle cx="750" cy="530" r="24" fill="var(--green-light)"/>
    <circle cx="770" cy="580" r="26" fill="var(--green-dark)"/>
    <circle cx="740" cy="606" r="11" fill="var(--green-light)"/>
    <rect x="0" y="995" width="770" height="94" fill="var(--green-dark)"/>
    <path d="M0 977 H226 Q240 977 244 992 L271 1089 H0 Z" fill="var(--green-light)"/>
  </svg>

  <div class="abs brand">
    <span class="brand-dot"></span>
    <span class="brand-name">Pflegedienst<br>Auenhaus</span>
  </div>

  <h1 class="abs headline">Ihrem verlässlichen Partner für individuelle und professionelle Pflege in Frankfurt</h1>

  <h2 class="abs tag">IHR WOHL AN ERSTER STELLE</h2>
  <p class="abs intro">Wir erhalten und fördern die Selbstständigkeit unserer Patienten und berücksichtigen ihre individuellen körperlichen, psychologischen und kulturellen Bedürfnisse. Dabei schaffen wir eine vertrauensvolle Atmosphäre, in der sich unsere Klienten sicher und gut aufgehoben fühlen. Angehörige binden wir aktiv in pflegerische Entscheidungen ein und stehen ihnen beratend zur Seite. Mit Respekt, Professionalität und Einfühlungsvermögen begleiten wir unsere Patienten zuverlässig in jeder Lebensphase – von der Unterstützung im Alltag bis zur einfühlsamen Begleitung in schwierigen Momenten.</p>

  <h2 class="abs section-title">UNSERE LEISTUNGEN</h2>
  <p class="abs section-lead">Wir bieten Ihnen individuelle Pflege und Betreuung in Ihrer gewohnten Häuslichkeit. Unser Ziel ist es,<br>Sie dabei zu unterstützen, so lange wie möglich selbstständig und sicher in Ihrem Zuhause zu leben.</p>

  <section class="abs card" style="left:39px">
    <h3 class="card-title">Leistungen der<br>Pflegekasse nach SGB XI</h3>
    <span class="card-rule"></span>
    <p class="card-text">Unsere Leistungen für die Pflegekasse umfassen Grundpflege, häusliche Betreuung, Verhinderungspflege und hauswirtschaftliche Hilfe. Wir unterstützen Sie bei der Körperpflege, dem Toilettengang, dem An- und Auskleiden sowie der Nahrungsaufnahme.</p>
  </section>
  <section class="abs card" style="left:273px">
    <h3 class="card-title">Leistungen der<br>Krankenkasse nach SGB V</h3>
    <span class="card-rule"></span>
    <p class="card-text">Unsere Leistungen für die Pflegekasse umfassen Grundpflege, häusliche Betreuung, Verhinderungspflege und hauswirtschaftliche Hilfe. Wir unterstützen Sie bei der Körperpflege, dem Toilettengang, dem An- und Auskleiden sowie der Nahrungsaufnahme.</p>
  </section>
  <section class="abs card" style="left:508px">
    <h3 class="card-title" style="top:53px">Pflegeberatung und<br>Beratungseinsätze</h3>
    <span class="card-rule"></span>
    <p class="card-text">Pflegebedürftige, die Pflegegeld beziehen, sind verpflichtet, regelmäßig eine Beratung in ihrer häuslichen Umgebung in Anspruch zu nehmen. Ebenso können Personen, die Pflegesachleistungen eines ambulanten Pflegedienstes nutzen, alle sechs Monate eine Pflegeberatung durchführen lassen.</p>
  </section>

  <svg class="service-icons" width="770" height="1089" viewBox="0 0 770 1089" aria-hidden="true">
    <g>
      <circle cx="150" cy="641" r="44" fill="var(--green-light)"/>
      <circle cx="150" cy="641" r="39" fill="var(--green-dark)"/>
      <g fill="none" stroke="var(--white)" stroke-width="4" stroke-linecap="round" stroke-linejoin="round">
        <path d="M128 634 V650 Q134 662 146 664"/>
        <path d="M172 634 V650 Q166 662 154 664"/>
      </g>
      <circle cx="150" cy="626" r="5" fill="var(--white)"/>
      <rect x="144" y="633" width="12" height="18" rx="4" fill="var(--white)"/>
    </g>
    <g>
      <circle cx="385" cy="641" r="44" fill="var(--green-light)"/>
      <circle cx="385" cy="641" r="39" fill="var(--green-dark)"/>
      <path d="M361 641 L385 620 L409 641 M367 637 V662 H403 V637" fill="none" stroke="var(--white)" stroke-width="5" stroke-linejoin="round" stroke-linecap="round"/>
      <path d="M385 656 L377 648 Q372 642 378 638 Q383 636 385 641 Q387 636 392 638 Q398 642 393 648 Z" fill="var(--white)"/>
    </g>
    <g>
      <circle cx="620" cy="641" r="44" fill="var(--green-light)"/>
      <circle cx="620" cy="641" r="39" fill="var(--green-dark)"/>
      <circle cx="620" cy="632" r="11" fill="var(--white)"/>
      <path d="M600 662 Q604 646 620 646 Q636 646 640 662 Z" fill="var(--white)"/>
      <path d="M606 632 Q606 616 620 616 Q634 616 634 632" fill="none" stroke="var(--white)" stroke-width="3"/>
    </g>
  </svg>

  <p class="abs claim">IHR* VERLÄSSLICHER <span>PARTNER</span></p>

  <div class="abs contact-call">
    <p class="label">Kontaktieren Sie uns</p>
    <p class="phone">
      <svg width="18" height="18" viewBox="0 0 18 18"><circle cx="9" cy="9" r="9" fill="var(--white)"/><path d="M6 4.5 L7.6 4.5 L8.3 7 L7.2 7.9 Q8 10 10.1 10.8 L11 9.7 L13.5 10.4 L13.5 12 Q13 13.5 11 13.2 Q5.5 12 4.8 7 Q4.5 5 6 4.5 Z" fill="var(--green-light)"/></svg>
      069/48201957
    </p>
  </div>

  <ul class="abs contact-list" style="left:292px">
    <li><svg width="12" height="12" viewBox="0 0 12 12"><circle cx="6" cy="6" r="6" fill="var(--white)"/><rect x="3" y="4" width="6" height="4.4" fill="none" stroke="var(--green-dark)" stroke-width="1"/><path d="M3 4 L6 6.4 L9 4" fill="none" stroke="var(--green-dark)" stroke-width="1"/></svg>info@pflegedienst-auenhaus.de</li>
    <li><svg width="12" height="12" viewBox="0 0 12 12"><circle cx="6" cy="6" r="6" fill="var(--white)"/><circle cx="6" cy="6" r="3.3" fill="none" stroke="var(--green-dark)" stroke-width="1"/><path d="M2.7 6 H9.3 M6 2.7 V9.3" stroke="var(--green-dark)" stroke-width="1"/></svg>www.pflegedienst-auenhaus.de</li>
  </ul>
  <ul class="abs contact-list" style="left:566px">
    <li><svg width="12" height="15" viewBox="0 0 12 15"><path d="M6 15 Q0 8 0 6 A6 6 0 0 1 12 6 Q12 8 6 15 Z" fill="var(--white)"/><circle cx="6" cy="6" r="2.3" fill="var(--green-dark)"/></svg>Lindenweg 12</li>
    <li class="plain">65931 Frankfurt am Main</li>
  </ul>
</main>
</body>
</html>
```